New Dental Office Needs an Attractive and user friendly Website Designed

I need a website for a new dental office. The Name is Larkhaven Dentistry. I would like a Modern design with a user friendly interface and usability.
I would like a landing page, a page that lists the services we offer: Cosmetic Dentistry, Implants, Dental Hygiene, Emergency Services, Restorations, Dentures
Target Market(s)
Mid to upper class
Industry/Entity Type
Dentistry
Coding
Coded - Design and coding required
Number of Pages Required
1 page
Requirements
Must have
- Landing page that has a scheduling option, Procedures, operating hours, and contact us info
Nice to have
- Appealing design, Soft comforting colors. Easy to navigate page, Modern and professional.

```html
<!DOCTYPE html>
<html lang="en">
<head>
<meta charset="UTF-8">
<title>Larkhaven Dentistry</title>
<link href="https://fonts.googleapis.com/css2?family=DM+Serif+Display&family=Inter:wght@400;500;600&display=swap" rel="stylesheet">
<style>
:root{
  --ink:#161a2e;
  --text:#3b3f52;
  --muted:#6b6f80;
  --blue:#5b95f0;
  --blue-soft:#eef3fc;
  --blue-card:#e9f0fc;
  --line:#d9dde6;
  --white:#ffffff;
  --dark:#1e1e1e;
}
*{box-sizing:border-box;margin:0;padding:0}
html,body{width:1200px;height:4800px;overflow:hidden}
body{position:relative;background:var(--white);font-family:'Inter',sans-serif;color:var(--text)}
.abs{position:absolute}
.serif{font-family:'DM Serif Display',serif;color:var(--ink);font-weight:400}
.logo{font-family:'Inter',sans-serif;font-weight:600;color:var(--ink);font-size:24px;display:flex;align-items:center;gap:10px}
.logo .dot{width:14px;height:14px;border-radius:50%;background:var(--blue)}
.btn{display:inline-flex;align-items:center}
.btn .pill{background:var(--dark);color:#fff;font-size:15px;font-weight:500;height:46px;padding:0 38px;border-radius:23px;display:flex;align-items:center}
.btn .arrow{width:46px;height:46px;border-radius:50%;background:var(--dark);border:2px solid #fff;display:flex;align-items:center;justify-content:center;margin-left:-6px}
.arrow-dot{width:44px;height:44px;border-radius:50%;background:var(--dark);display:flex;align-items:center;justify-content:center}
.label{font-family:'DM Serif Display',serif;color:var(--blue);font-size:15px}

/* header */
.nav{top:0;left:0;width:1200px;height:80px}
.nav .links{position:absolute;right:310px;top:28px;display:flex;gap:56px;font-size:14px;color:var(--ink)}
.nav .links .on{text-decoration:underline;text-underline-offset:6px}
.nav .contact{position:absolute;left:955px;top:15px;width:160px;height:46px;border-radius:23px;background:var(--dark);color:#fff;font-size:14px;font-weight:500;display:flex;align-items:center;justify-content:center}

/* hero */
.hero{left:17px;top:80px;width:1168px;height:580px;border-radius:30px;overflow:hidden;background:linear-gradient(100deg,#b9c3eb 0%,#d8d4ef 45%,#f6d0d8 80%,#f8dde2 100%)}
.hero h1{position:absolute;left:69px;top:110px;font-size:62px;line-height:66px;width:560px}
.hero .book{position:absolute;left:69px;top:332px}
.hero .thumb{position:absolute;left:68px;top:437px;width:160px;height:98px;border-radius:10px;background:linear-gradient(160deg,#f1e6c8,#e8c76a)}
.hero .quote{position:absolute;left:246px;top:437px;width:240px;font-size:15px;line-height:24px;color:var(--ink)}
.hero .quote b{display:block;color:var(--blue);font-family:'DM Serif Display',serif;font-size:36px;line-height:26px;height:26px}
.hero .dots{position:absolute;left:248px;top:547px;display:flex;gap:12px}
.hero .dots i{width:6px;height:6px;border-radius:50%;border:1px solid var(--ink)}
.hero .dots i:first-child{background:var(--ink)}
.hero .photo{position:absolute;left:630px;top:55px;width:460px;height:525px;border-radius:220px 220px 0 0;background:linear-gradient(180deg,#c8a08c 0%,#5b96d9 45%,#3d78c7 100%)}
.hero .office{position:absolute;left:593px;top:340px;width:118px;height:118px;border-radius:50%;background:rgba(255,255,255,.75);display:flex;align-items:center;justify-content:center;font-size:15px;color:var(--ink)}

/* services */
.services{left:0;top:660px;width:1200px;height:900px;background:linear-gradient(180deg,#fff 0%,#f3f6fd 30%,var(--blue-soft) 100%)}
.services h2{position:absolute;left:86px;top:70px;font-size:50px}
.services .intro{position:absolute;left:622px;top:86px;width:500px;font-size:15px;line-height:26px}
.card{position:absolute;width:324px;height:304px;background:#fff;padding:24px 30px}
.card .ico{width:54px;height:60px}
.card h3{font-family:'DM Serif Display',serif;font-size:22px;color:var(--ink);font-weight:400;margin:20px 0 12px}
.card p{font-size:15px;line-height:26px;width:270px}
.card .arrow-dot{position:absolute;left:30px;top:228px}

/* about */
.about{left:0;top:1560px;width:1200px;height:730px}
.about .label{position:absolute;left:84px;top:145px}
.about h2{position:absolute;left:84px;top:170px;font-size:50px;line-height:56px;width:520px}
.about p{position:absolute;left:84px;top:365px;width:500px;font-size:16px;line-height:27px}
.about .learn{position:absolute;left:84px;top:505px}
.about .call{position:absolute;left:318px;top:503px}
.about .call small{display:flex;align-items:center;gap:16px;font-size:12px;color:var(--ink)}
.about .call small i{width:44px;height:1px;background:var(--muted)}
.about .call a{display:block;margin-left:58px;margin-top:6px;color:var(--blue);font-size:22px;text-decoration:underline}
.about .photo{position:absolute;left:633px;top:132px;width:444px;height:460px;border-radius:0 0 222px 222px;background:linear-gradient(135deg,#6a5c55 0%,#c7a99a 40%,#3a5b86 100%)}

/* booking */
.booking{left:0;top:2290px;width:1200px;height:660px;background:var(--blue-soft)}
.cal{position:absolute;left:86px;top:110px;width:566px;height:428px;background:#fff;border:2px solid #d7dde9;padding:24px 42px}
.cal h4{font-size:14px;font-weight:600;color:var(--ink)}
.cal .month{position:absolute;left:42px;top:68px;font-size:10px;color:var(--ink)}
.cal .navs{position:absolute;left:246px;top:64px;font-size:13px;color:var(--ink);letter-spacing:18px}
.cal .grid{position:absolute;left:36px;top:98px;display:grid;grid-template-columns:repeat(7,37px);row-gap:12px;font-size:9px;text-align:center;color:var(--ink)}
.cal .grid .h{font-size:7px;font-weight:600}
.cal .grid span{width:24px;height:24px;margin:0 auto;border-radius:50%;display:flex;align-items:center;justify-content:center}
.cal .grid .av{background:var(--blue-card);color:var(--blue)}
.cal .grid .sel{background:var(--blue);color:#fff}
.cal .tz{position:absolute;left:40px;top:318px;font-size:8px;color:var(--muted)}
.cal .day{position:absolute;left:326px;top:68px;font-size:10px;color:var(--ink)}
.cal .slots{position:absolute;left:326px;top:96px;display:flex;flex-direction:column;gap:10px}
.slot{width:164px;height:28px;border:2px solid var(--blue);border-radius:3px;color:var(--blue);font-size:10px;display:flex;align-items:center;justify-content:center}
.slot-pick{display:flex;gap:10px}
.slot-pick span{width:77px;height:28px;border-radius:3px;font-size:10px;display:flex;align-items:center;justify-content:center}
.slot-pick .t{background:var(--dark);color:#fff}
.slot-pick .c{background:#8fb7f5;color:#fff}
.cal .bar{position:absolute;left:516px;top:128px;width:3px;height:145px;background:#bcc3cf;border-radius:2px}
.booking h2{position:absolute;left:698px;top:205px;font-size:50px}
.booking p{position:absolute;left:698px;top:283px;width:410px;font-size:16px;line-height:26px}
.booking .btn{position:absolute;left:700px;top:388px}

/* procedures */
.procedures{left:0;top:2950px;width:1200px;height:700px}
.procedures .label{position:absolute;left:0;width:1200px;text-align:center;top:97px}
.procedures h2{position:absolute;left:0;width:1200px;text-align:center;top:118px;font-size:50px}
.step{position:absolute;top:228px;width:332px;height:370px;border:1px solid #d3d9e5;border-radius:16px;overflow:hidden;text-align:center;background:#fff}
.step .top{height:190px;background:var(--blue-card);display:flex;align-items:center;justify-content:center}
.step small{display:block;margin-top:22px;font-size:12px;letter-spacing:3px;color:var(--blue);font-weight:500}
.step h3{font-family:'DM Serif Display',serif;font-weight:400;color:var(--ink);font-size:22px;margin:12px 0 8px}
.step p{font-size:15px;line-height:26px;width:270px;margin:0 auto}

/* contact */
.contact{left:0;top:3650px;width:1200px;height:655px;background:var(--blue-soft)}
.contact .label{position:absolute;left:84px;top:165px}
.contact h2{position:absolute;left:84px;top:195px;font-size:48px;line-height:56px;width:580px}
.contact p{position:absolute;left:84px;top:330px;width:520px;font-size:16px;line-height:27px}
.contact .info{position:absolute;left:84px;top:424px;display:flex;gap:44px;font-size:16px;color:var(--ink);font-weight:500}
.contact .info div{display:flex;align-items:center;gap:14px}
.ci{width:42px;height:42px;border-radius:50%;background:var(--blue);display:flex;align-items:center;justify-content:center}
.form{position:absolute;left:666px;top:3600px;width:452px;height:630px;background:#fff;border:1px solid #d6dbe6;border-radius:6px;padding:62px 28px}
.form .row{display:flex;gap:16px;margin-bottom:24px}
.field{flex:1}
.field label{display:block;font-size:15px;font-weight:500;color:var(--ink);margin-bottom:6px}
.field .in{height:46px;border:1px solid var(--line);border-radius:3px;font-size:12px;color:var(--text);padding:0 12px;display:flex;align-items:center;justify-content:space-between}
.field .area{height:168px;border:1px solid var(--line);border-radius:3px;font-size:12px;padding:14px 12px}
.form .btn{margin-top:20px}

/* footer */
.footer{left:0;top:4305px;width:1200px;height:495px}
.footer h5{font-family:'DM Serif Display',serif;font-weight:400;font-size:19px;color:var(--ink);margin-bottom:24px}
.fcol{position:absolute;top:102px;font-size:15px;line-height:26px}
.sub{display:flex;margin-top:26px;height:48px;border:1px solid var(--line);border-radius:24px;width:300px;align-items:center;padding-left:18px;font-size:13px;justify-content:space-between}
.sub span:last-child{background:var(--dark);color:#fff;height:46px;border-radius:23px;padding:0 26px;display:flex;align-items:center;font-size:14px;font-weight:500}
.hours div{display:flex;margin-bottom:10px}
.hours div span:first-child{width:195px}
.cline{display:flex;gap:10px;margin-bottom:10px;align-items:flex-start}
.cline svg{margin-top:6px;flex:none}
.footer .rule{position:absolute;left:84px;top:400px;width:1032px;height:1px;background:var(--line)}
.footer .bottom{position:absolute;left:84px;top:440px;width:1032px;display:flex;align-items:center;font-size:12px;color:var(--text)}
.social{display:flex;gap:14px;margin-left:30px}
.social i{width:18px;height:18px;border-radius:50%;background:var(--ink)}
</style>
</head>
<body>

<header class="abs nav">
  <div class="logo abs" style="left:84px;top:24px"><span class="dot"></span>Larkhaven Dentistry</div>
  <nav class="links"><span class="on">Home</span><span>About Us</span><span>Services</span><span>Procedures</span></nav>
  <div class="contact">Contact Us</div>
</header>

<section class="abs hero">
  <h1 class="serif">Your great smile beging with a great dentist</h1>
  <div class="btn book"><span class="pill">Book Appointment</span><span class="arrow"><svg width="14" height="14" viewBox="0 0 14 14"><path d="M3 11L11 3M5 3h6v6" stroke="#fff" stroke-width="1.6" fill="none"/></svg></span></div>
  <div class="thumb" role="img" aria-label="Photo of a smiling patient"></div>
  <div class="quote"><b>“</b>Lorem ipsdolor sit , consetur adipiscing elit. Cras eleifend ante in posuere.</div>
  <div class="dots"><i></i><i></i><i></i></div>
  <div class="photo" role="img" aria-label="Photo of a cheerful dentist holding dental tools"></div>
  <div class="office">Dental Office</div>
</section>

<section class="abs services">
  <h2 class="serif">What Service We Offer</h2>
  <p class="intro">Lorem ipsum dolor sit amet, consectetur adipiscing elit. Cras eleifend ante in e blandit posuere. Cras ipsum massa,</p>

  <div class="card" style="left:84px;top:183px">
    <svg class="ico" viewBox="0 0 54 60"><path d="M2 2h50v40L27 58 2 42z" fill="var(--blue)"/><path d="M14 26q13-10 26 0q-13 10-26 0z" stroke="#fff" stroke-width="2" fill="none"/></svg>
    <h3>Cosmetic Dentistry</h3><p>Suspendisse eget lectus a elit sagittis ultrices. In tristique nibh ut vulputate imperdiet.</p>
    <span class="arrow-dot"><svg width="12" height="12" viewBox="0 0 14 14"><path d="M3 11L11 3M5 3h6v6" stroke="#fff" stroke-width="1.6" fill="none"/></svg></span>
  </div>
  <div class="card" style="left:438px;top:183px">
    <svg class="ico" viewBox="0 0 54 60"><path d="M2 2h50v40L27 58 2 42z" fill="var(--blue)"/><path d="M18 16h18v8H18zM22 24h10l-2 16h-6z" stroke="#fff" stroke-width="2" fill="none"/></svg>
    <h3>Implants</h3><p>Suspendisse eget lectus a elit sagittis ultrices. In tristique nibh ut vulputate imperdiet.</p>
    <span class="arrow-dot"><svg width="12" height="12" viewBox="0 0 14 14"><path d="M3 11L11 3M5 3h6v6" stroke="#fff" stroke-width="1.6" fill="none"/></svg></span>
  </div>
  <div class="card" style="left:792px;top:183px">
    <svg class="ico" viewBox="0 0 54 60"><path d="M2 2h50v40L27 58 2 42z" fill="var(--blue)"/><path d="M17 18q10-6 20 0q2 10-4 20l-3-8h-6l-3 8q-6-10-4-20z" stroke="#fff" stroke-width="2" fill="none"/></svg>
    <h3>Dental Hygiene</h3><p>Suspendisse eget lectus a elit sagittis ultrices. In tristique nibh ut vulputate imperdiet.</p>
    <span class="arrow-dot"><svg width="12" height="12" viewBox="0 0 14 14"><path d="M3 11L11 3M5 3h6v6" stroke="#fff" stroke-width="1.6" fill="none"/></svg></span>
  </div>
  <div class="card" style="left:84px;top:530px">
    <svg class="ico" viewBox="0 0 54 60"><path d="M2 2h50v40L27 58 2 42z" fill="var(--blue)"/><path d="M16 14h14v14H16zM24 24h14v14H24z" stroke="#fff" stroke-width="2" fill="none"/></svg>
    <h3>Emergency Services</h3><p>Suspendisse eget lectus a elit sagittis ultrices. In tristique nibh ut vulputate imperdiet.</p>
    <span class="arrow-dot"><svg width="12" height="12" viewBox="0 0 14 14"><path d="M3 11L11 3M5 3h6v6" stroke="#fff" stroke-width="1.6" fill="none"/></svg></span>
  </div>
  <div class="card" style="left:438px;top:530px">
    <svg class="ico" viewBox="0 0 54 60"><path d="M2 2h50v40L27 58 2 42z" fill="var(--blue)"/><path d="M14 18h26v8H14zM18 26q9 4 18 0l-3 12h-12z" stroke="#fff" stroke-width="2" fill="none"/></svg>
    <h3>Restorations</h3><p>Suspendisse eget lectus a elit sagittis ultrices. In tristique nibh ut vulputate imperdiet.</p>
    <span class="arrow-dot"><svg width="12" height="12" viewBox="0 0 14 14"><path d="M3 11L11 3M5 3h6v6" stroke="#fff" stroke-width="1.6" fill="none"/></svg></span>
  </div>
  <div class="card" style="left:792px;top:530px">
    <svg class="ico" viewBox="0 0 54 60"><path d="M2 2h50v40L27 58 2 42z" fill="var(--blue)"/><rect x="12" y="18" width="30" height="14" rx="4" stroke="#fff" stroke-width="2" fill="none"/><path d="M19 18v14M27 18v14M35 18v14" stroke="#fff" stroke-width="1.5"/></svg>
    <h3>Dentures</h3><p>Suspendisse eget lectus a elit sagittis ultrices. In tristique nibh ut vulputate imperdiet.</p>
    <span class="arrow-dot"><svg width="12" height="12" viewBox="0 0 14 14"><path d="M3 11L11 3M5 3h6v6" stroke="#fff" stroke-width="1.6" fill="none"/></svg></span>
  </div>
</section>

<section class="abs about">
  <span class="label">About</span>
  <h2 class="serif">Transform your smile with state-of-the Larkhaven Dentistry</h2>
  <p>Lorem ipsum dolor sit amet, consectetur adipiscing elit, sed do eiusmod tempor incididunt ut labore et dolore magna aliqua. Quis ipsum suspendisse ultrices gravida. Risus commodo viverra maecenas accumsan lacus vel facilisis.</p>
  <div class="btn learn"><span class="pill">Learn More</span><span class="arrow"><svg width="14" height="14" viewBox="0 0 14 14"><path d="M3 11L11 3M5 3h6v6" stroke="#fff" stroke-width="1.6" fill="none"/></svg></span></div>
  <div class="call"><small><i></i>Book Appointment</small><a>(555) 010-2468</a></div>
  <div class="photo" role="img" aria-label="Photo of a smiling patient during a dental check-up"></div>
  <svg class="abs" style="left:600px;top:450px" width="520" height="250" viewBox="0 0 520 250">
    <path d="M12 0A248 205 0 0 0 494 0" stroke="var(--blue)" stroke-width="12" fill="none" stroke-linecap="round" transform="translate(0,30)"/>
    <circle cx="494" cy="18" r="10" fill="var(--blue)"/>
  </svg>
</section>

<section class="abs booking">
  <div class="cal">
    <h4>Select a Date &amp; Time</h4>
    <span class="month">May 2025</span>
    <span class="navs">‹›</span>
    <div class="grid">
      <div class="h">MON</div><div class="h">TUE</div><div class="h">WED</div><div class="h">THU</div><div class="h">FRI</div><div class="h">SAT</div><div class="h">SUN</div>
      <span></span><span></span><span></span><span>1</span><span class="av">2</span><span class="av">3</span><span class="av">4</span>
      <span>5</span><span class="av">6</span><span class="av">7</span><span class="av">8</span><span class="sel">9</span><span class="av">10</span><span class="av">11</span>
      <span>12</span><span class="av">13</span><span class="av">14</span><span class="av">15</span><span class="av">16</span><span class="av">17</span><span class="av">18</span>
      <span>19</span><span class="av">20</span><span class="av">21</span><span class="av">22</span><span class="av">23</span><span class="av">24</span><span class="av">25</span>
      <span>26</span><span class="av">27</span><span class="av">28</span><span class="av">29</span><span class="av">30</span><span class="av">31</span><span></span>
    </div>
    <span class="tz">◉ Local Standard Time (8:39 pm) ⌄</span>
    <span class="day">Thursday, May 9</span>
    <div class="slots">
      <div class="slot">10:30am</div><div class="slot">11:00am</div>
      <div class="slot-pick"><span class="t">11:30am</span><span class="c">Confirm</span></div>
      <div class="slot">12:00pm</div><div class="slot">12:30pm</div><div class="slot">01:00pm</div><div class="slot">01:30pm</div><div class="slot">02:00pm</div>
    </div>
    <span class="bar"></span>
  </div>
  <h2 class="serif">Booking Schedule</h2>
  <p>Duis finibus, eros congue iaculis blandit, nunc dui tempor libero, quis porta elit diam vitae nisl. Praesent laoreet, nisl dictum lacinia ornare</p>
  <div class="btn"><span class="pill">Book Now</span><span class="arrow"><svg width="14" height="14" viewBox="0 0 14 14"><path d="M3 11L11 3M5 3h6v6" stroke="#fff" stroke-width="1.6" fill="none"/></svg></span></div>
</section>

<section class="abs procedures">
  <span class="label">Procedures</span>
  <h2 class="serif">Procedure for Appointment</h2>
  <div class="step" style="left:84px">
    <div class="top"><svg width="84" height="96" viewBox="0 0 84 96" fill="none" stroke="var(--blue)" stroke-width="2"><circle cx="42" cy="36" r="18"/><path d="M20 40V34a22 22 0 0 1 44 0v6M20 34h6v12h-6zM58 34h6v12h-6zM64 46q0 12-16 12M12 92q0-24 30-24t30 24z"/></svg></div>
    <small>STEP 01</small><h3>Call Or Mail Us</h3><p>Risus commodo viverra maecenas accumsan lacus vel facilisis.</p>
  </div>
  <div class="step" style="left:434px">
    <div class="top"><svg width="86" height="86" viewBox="0 0 86 86" fill="none" stroke="var(--blue)" stroke-width="2"><rect x="4" y="10" width="62" height="58" rx="4"/><path d="M4 24h62M16 4v12M54 4v12"/><circle cx="62" cy="62" r="18" fill="#fff"/><path d="M54 62l6 6 10-12"/><path d="M14 34h6M28 34h6M42 34h6M14 46h6M28 46h6M14 58h6M28 58h6" stroke-width="3"/></svg></div>
    <small>STEP 02</small><h3>Choose Date and Time</h3><p>Risus commodo viverra maecenas accumsan lacus vel facilisis.</p>
  </div>
  <div class="step" style="left:784px">
    <div class="top"><svg width="90" height="90" viewBox="0 0 90 90" fill="none" stroke="var(--blue)" stroke-width="2"><path d="M36 30q12-8 24 0q12-8 18 6q2 18-8 44q-4 6-8-4l-4-14q-4-4-8 0l-4 14q-4 10-8 4q-10-26-8-44q4-12 6-6z"/><path d="M22 8v14M15 15h14M10 34v10M5 39h10M36 4v8M32 8h8"/></svg></div>
    <small>STEP 03</small><h3>Come for Treatment</h3><p>Risus commodo viverra maecenas accumsan lacus vel facilisis.</p>
  </div>
</section>

<section class="abs contact">
  <span class="label">Contact Us</span>
  <h2 class="serif">Get in touch to book your first appointment</h2>
  <p>Phasellus ultricies libero nec bibendum congue. Donec dolor ligula, pulvinar vulputate erat eget, feugiat lobortis nulla.</p>
  <div class="info">
    <div><span class="ci"><svg width="18" height="18" viewBox="0 0 24 24"><path d="M5 3h4l2 5-3 2a12 12 0 0 0 6 6l2-3 5 2v4a2 2 0 0 1-2 2A18 18 0 0 1 3 5a2 2 0 0 1 2-2z" fill="#fff"/></svg></span>(555) 010-2468</div>
    <div><span class="ci"><svg width="18" height="14" viewBox="0 0 18 14"><rect x="1" y="1" width="16" height="12" rx="1" fill="#fff"/><path d="M1 2l8 6 8-6" stroke="var(--blue)" stroke-width="1.5" fill="none"/></svg></span>info@larkhavendentistry.com</div>
  </div>
</section>

<form class="form">
  <div class="row">
    <div class="field"><label>Name</label><div class="in">Full Name</div></div>
    <div class="field"><label>Email</label><div class="in">you@example.com</div></div>
  </div>
  <div class="row">
    <div class="field"><label>Phone Number</label><div class="in">(555) 010-2468</div></div>
    <div class="field"><label>Service</label><div class="in">Select a service <span>▾</span></div></div>
  </div>
  <div class="field"><label>Message</label><div class="area">Please describe what service your are interested in…</div></div>
  <div class="btn"><span class="pill">Submit Now</span><span class="arrow"><svg width="14" height="14" viewBox="0 0 14 14"><path d="M3 11L11 3M5 3h6v6" stroke="#fff" stroke-width="1.6" fill="none"/></svg></span></div>
</form>

<footer class="abs footer">
  <div class="fcol" style="left:84px;width:320px">
    <h5>Subscribe to our Newsletter</h5>
    <p>Donec dolor ligula, pulvinar vulputate erat eget, feugiat lobortis nulla.</p>
    <div class="sub"><span>Enter your email</span><span>Submit Now</span></div>
  </div>
  <div class="fcol hours" style="left:488px">
    <h5>Operating Hours</h5>
    <div><span>Monday - Wednesday</span><span>10:00 am</span></div>
    <div><span>Thursday - Saturday</span><span>02:00 pm</span></div>
  </div>
  <div class="fcol" style="left:852px;width:270px">
    <h5>Contact</h5>
    <div class="cline"><svg width="12" height="14" viewBox="0 0 12 14"><path d="M6 14s5-5 5-8.5A5 5 0 0 0 1 5.5C1 9 6 14 6 14z" fill="var(--blue)"/><circle cx="6" cy="5.5" r="2" fill="#fff"/></svg><span>18 Meadowlark Lane Charlotte NC 28205, USA</span></div>
    <div class="cline"><svg width="14" height="14" viewBox="0 0 24 24"><path d="M5 3h4l2 5-3 2a12 12 0 0 0 6 6l2-3 5 2v4a2 2 0 0 1-2 2A18 18 0 0 1 3 5a2 2 0 0 1 2-2z" fill="var(--blue)"/></svg><span>(555) 010-2468</span></div>
    <div class="cline"><svg width="14" height="12" viewBox="0 0 18 14"><rect x="1" y="1" width="16" height="12" rx="1" fill="var(--blue)"/><path d="M1 2l8 6 8-6" stroke="#fff" stroke-width="1.5" fill="none"/></svg><span>info@larkhavendentistry.com</span></div>
  </div>
  <div class="rule"></div>
  <div class="bottom">
    <div class="logo" style="font-size:20px"><span class="dot"></span>Larkhaven Dentistry</div>
    <div class="social"><i></i><i></i><i></i><i></i><i></i></div>
    <span style="margin-left:136px">© 2025 Larkhaven Dentistry. All right reserved</span>
    <span style="margin-left:auto">May 24, 2025.</span>
  </div>
</footer>

</body>
</html>
```